Business Card Design Project

Name: Kunle O. Edet
Designation: Partner
Address: QRM Building, 14 Harmony Close, P.O. Box 58314, Victoria Island Lagos, Nigeria
Tel: +234 1 7395162
mobile: +234 1 7061527394
Email: koedet@larkmoorassociates.com
website www.larkmoorassociates.com

```html
<!DOCTYPE html>
<html lang="en">
<head>
<meta charset="utf-8">
<title>Larkmoor Associates – Business Card</title>
<link rel="stylesheet" href="https://fonts.googleapis.com/css2?family=Arimo:wght@400;700&family=Tinos&display=swap">
<style>
  :root {
    --page-bg: #ffffff;
    --heading: #111111;
    --card-dark: #181818;
    --card-light: #ffffff;
    --card-border: #000000;
    --silver: #c4c4c8;
    --mark-grey: #8a8a8e;
    --ink: #111111;
    --body-text: #333333;
  }
  * { margin: 0; padding: 0; box-sizing: border-box; }
  html, body {
    width: 1200px; height: 590px; overflow: hidden;
    background: var(--page-bg);
  }
  .sheet { position: relative; width: 1200px; height: 590px; }

  .side-label {
    position: absolute;
    font: 700 19px/1 "Arimo", Arial, sans-serif;
    color: var(--heading);
    transform: translateX(-50%);
  }
  .side-label--front { left: 359px; top: 90px; }
  .side-label--back { left: 782px; top: 89px; }

  .card { position: absolute; width: 365px; height: 211px; }
  .card--front { left: 212px; top: 128px; background: var(--card-dark); }
  .card--back {
    left: 637px; top: 127px; width: 364px; height: 211px;
    background: var(--card-light); border: 1px solid var(--card-border);
  }

  /* Front wordmark */
  .brand-front__dot {
    position: absolute; left: 148px; top: 40px;
    width: 68px; height: 68px; border-radius: 50%;
    background: var(--mark-grey);
  }
  .brand-front__name, .brand-front__sub {
    position: absolute;
    font-family: "Arimo", Arial, sans-serif; font-weight: 700;
    color: var(--silver); line-height: 1; white-space: nowrap;
  }
  .brand-front__name { left: 90px; top: 115px; font-size: 33px; }
  .brand-front__sub { left: 170px; top: 147px; font-size: 15px; }

  /* Back side */
  .holder-name {
    position: absolute; left: 10px; top: 14px;
    font: 400 19px/1 "Tinos", "Times New Roman", serif; color: var(--ink);
  }
  .holder-role {
    position: absolute; left: 15px; top: 38px;
    font: 400 16px/1 "Tinos", "Times New Roman", serif; color: var(--ink);
  }
  .address {
    position: absolute; left: 13px; top: 82px;
    font: 400 12px/15px "Arimo", Arial, sans-serif; color: var(--body-text);
    font-style: normal;
  }
  .address__rule {
    position: absolute; left: 14px; top: 139px;
    width: 172px; height: 1px; background: var(--ink);
  }
  .contact {
    position: absolute; left: 9px; top: 141px;
    list-style: none;
    font: 400 12px/1 "Arimo", Arial, sans-serif; color: var(--body-text);
  }
  .contact__item { display: flex; align-items: center; height: 17px; gap: 5px; }
  .contact__icon { width: 17px; height: 15px; flex: none; }
  .contact__item--web { padding-left: 10px; }

  .brand-back__dot {
    position: absolute; left: 272px; top: 14px;
    width: 44px; height: 44px; border-radius: 50%;
    background: var(--mark-grey);
  }
  .brand-back__name, .brand-back__sub {
    position: absolute;
    font-family: "Arimo", Arial, sans-serif; font-weight: 700;
    color: var(--ink); line-height: 1; white-space: nowrap;
  }
  .brand-back__name { left: 249px; top: 64px; font-size: 20px; }
  .brand-back__sub { left: 263px; top: 89px; font-size: 15px; }
</style>
</head>
<body>
<main class="sheet">
  <h2 class="side-label side-label--front">Front Side</h2>
  <h2 class="side-label side-label--back">Back Side</h2>

  <section class="card card--front" aria-label="Card front">
    <span class="brand-front__dot"></span>
    <span class="brand-front__name">Larkmoor</span>
    <span class="brand-front__sub">Associates</span>
  </section>

  <section class="card card--back" aria-label="Card back">
    <p class="holder-name">Kunle O. Edet</p>
    <p class="holder-role">Partner</p>

    <address class="address">
      QRM Building,<br>
      14 Harmony Close,<br>
      P.O. Box 58314,<br>
      Victoria Island Lagos, Nigeria
    </address>
    <span class="address__rule"></span>

    <ul class="contact">
      <li class="contact__item">
        <svg class="contact__icon" viewBox="0 0 17 15" aria-hidden="true">
          <circle cx="8.5" cy="7.5" r="7" fill="none" stroke="#111" stroke-width="1.2"/>
          <path d="M5.6 4.2c.6-.5 1.2-.4 1.5.1l.7 1.2c.2.4 0 .8-.3 1l-.5.3c.3.9 1 1.7 1.9 2.2l.4-.4c.3-.3.7-.3 1 0l1 .9c.4.4.3 1-.2 1.4-1 .8-2.4.5-3.8-.6C5.9 8.9 5.1 7.4 5.1 6c0-.7.2-1.3.5-1.8z" fill="#111"/>
        </svg>
        <span>+234 1 7395162</span>
      </li>
      <li class="contact__item">
        <svg class="contact__icon" viewBox="0 0 17 15" aria-hidden="true">
          <rect x="5" y="1" width="7" height="13" rx="1" fill="none" stroke="#111" stroke-width="1.3"/>
          <rect x="6.5" y="3" width="4" height="4" fill="#111"/>
          <circle cx="8.5" cy="11" r="1" fill="#111"/>
        </svg>
        <span>+234 1 7061527394</span>
      </li>
      <li class="contact__item">
        <svg class="contact__icon" viewBox="0 0 17 15" aria-hidden="true">
          <circle cx="10" cy="7.5" r="6.5" fill="none" stroke="#111" stroke-width="1.2"/>
          <text x="10" y="10.5" text-anchor="middle" font-family="Arimo, Arial, sans-serif" font-size="9" font-weight="700" fill="#111">@</text>
        </svg>
        <span>koedet@larkmoorassociates.com</span>
      </li>
      <li class="contact__item contact__item--web">
        <span>www.larkmoorassociates.com</span>
      </li>
    </ul>

    <span class="brand-back__dot"></span>
    <span class="brand-back__name">Larkmoor</span>
    <span class="brand-back__sub">Associates</span>
  </section>
</main>
</body>
</html>
```